A banner for a fully digital bank.

In need of banners for the “Q7 Bank”. Has to show us not as just another digital bank, but a bank in whom ordinary people can trust. We won’t charge overdraft fees, transaction fees etc as a normal stationary bank would. We also will work with crypto, and be as user friendly as possible.

Banking

```html
<!DOCTYPE html>
<html lang="en">
<head>
<meta charset="utf-8">
<title>Q7 Bank – Fully Digital Bank</title>
<link href="https://fonts.googleapis.com/css2?family=Josefin+Sans:wght@300;700&family=Oswald:wght@600&display=swap" rel="stylesheet">
<style>
  :root {
    --brand-red: #c70000;
    --button-red: #d80404;
    --button-edge: #a20000;
    --white: #ffffff;
    --divider: rgba(255, 255, 255, 0.55);
  }
  html, body {
    margin: 0;
    padding: 0;
    overflow: hidden;
    background: var(--brand-red);
  }
  .banner {
    position: relative;
    width: 1200px;
    height: 595px;
    overflow: hidden;
    background: var(--brand-red);
    color: var(--white);
    font-family: "Josefin Sans", sans-serif;
  }
  .brand-name {
    position: absolute;
    left: 120px;
    top: 84px;
    margin: 0;
    font-weight: 700;
    font-size: 146px;
    line-height: 1;
    letter-spacing: -3px;
    white-space: nowrap;
  }
  .speed-stripes {
    position: absolute;
    left: 818px;
    top: 66px;
    width: 382px;
    height: 164px;
  }
  .join-button {
    position: absolute;
    left: 836px;
    top: 92px;
    width: 334px;
    height: 98px;
    box-sizing: border-box;
    border-radius: 49px;
    background: var(--button-red);
    border: 4px solid var(--button-edge);
    display: flex;
    align-items: center;
    justify-content: center;
    font-family: "Oswald", sans-serif;
    font-weight: 600;
    font-size: 42px;
    letter-spacing: 1px;
    color: var(--white);
    text-decoration: none;
  }
  .tagline {
    position: absolute;
    left: 120px;
    top: 264px;
    margin: 0;
    font-weight: 300;
    font-size: 54px;
    letter-spacing: 7.5px;
    line-height: 1;
    white-space: nowrap;
  }
  .divider {
    position: absolute;
    left: 120px;
    top: 344px;
    width: 1008px;
    height: 3px;
    background: var(--divider);
  }
  .no-fees {
    position: absolute;
    left: 120px;
    top: 388px;
    margin: 0;
    line-height: 1;
    white-space: nowrap;
  }
  .no-fees .no {
    font-weight: 700;
    font-size: 58px;
    letter-spacing: 4px;
    margin-right: 30px;
  }
  .no-fees .fees {
    font-weight: 300;
    font-size: 42px;
    letter-spacing: 1px;
  }
  .features {
    position: absolute;
    left: 120px;
    top: 484px;
    margin: 0;
    font-weight: 700;
    font-size: 46px;
    letter-spacing: 0.5px;
    line-height: 1;
    white-space: nowrap;
  }
  .features .sep {
    margin: 0 36px;
  }
</style>
</head>
<body>
  <main class="banner">
    <h1 class="brand-name">Q7 BANK</h1>

    <svg class="speed-stripes" viewBox="0 0 382 164" aria-hidden="true">
      <g fill="#ffffff">
        <rect x="0"  y="0"   width="382" height="7"/>
        <rect x="2"  y="16"  width="380" height="7"/>
        <rect x="4"  y="32"  width="378" height="7"/>
        <rect x="6"  y="48"  width="376" height="7"/>
        <rect x="8"  y="64"  width="374" height="7"/>
        <rect x="10" y="80"  width="372" height="7"/>
        <rect x="12" y="96"  width="370" height="7"/>
        <rect x="14" y="112" width="368" height="7"/>
        <rect x="16" y="128" width="366" height="7"/>
        <rect x="18" y="144" width="364" height="7"/>
        <rect x="20" y="157" width="362" height="7"/>
      </g>
    </svg>

    <a class="join-button" href="#">JOIN US NOW</a>

    <p class="tagline">FULLY DIGITAL BANK</p>
    <div class="divider"></div>

    <p class="no-fees"><span class="no">NO</span><span class="fees">OVERDRAFT FEES | TRANSACTION FEES</span></p>
    <p class="features">WORK WITH CRYPTO<span class="sep">|</span>USER FRIENDLY</p>
  </main>
</body>
</html>
```